Verdant Medispa Business Card

need a business card for our medispa, attached please see the logo.
our website is https://verdantmedispa-example.com

Sorina Belcourt, MD
Internal Medicine

555-204-7193

Sorina@verdantmedispa-example.com

Www.Verdantmedispa-example.com

738 E Harlow Blvd N, Ste 512, Katy, TX 77981

Target Market(s)

MedSpa, Cosmetics, Esthetics

Industry/Entity Type

MedicalSpa

Contact Information for Business Card

Please see the attached business card which i pulled from the internet. I like the idea back as a logo and front with info.

Font styles to use
Decorative

Requirements
Must have
• Color should be matching with Logo and Website theme, Also I like to have QR code for the website

```html
<!DOCTYPE html>
<html lang="en">
<head>
<meta charset="utf-8">
<title>Verdant Medispa Business Card</title>
<link href="https://fonts.googleapis.com/css2?family=Montserrat:wght@400;500;700&display=swap" rel="stylesheet">
<style>
  :root {
    --page-bg: #d9d9d9;
    --card-white: #ffffff;
    --beige-light: #e6d9cf;
    --beige: #c7b09f;
    --beige-dark: #b39a87;
    --gold: #d3a52a;
    --band-brown: #7b6552;
    --ink: #1e1e1e;
    --qr-tint: #f4ecd6;
  }
  * { box-sizing: border-box; margin: 0; padding: 0; }
  html, body { width: 1200px; height: 813px; overflow: hidden; }
  body {
    background: var(--page-bg);
    font-family: "Montserrat", sans-serif;
    position: relative;
  }
  .card {
    position: absolute;
    width: 560px;
    height: 320px;
    border-radius: 22px;
    overflow: hidden;
    top: 246px;
    box-shadow: 0 6px 18px rgba(0,0,0,0.18);
  }
  /* Front face */
  .card-front {
    left: 30px;
    background: radial-gradient(ellipse at 55% 45%, var(--beige-light) 0%, var(--beige) 55%, var(--beige-dark) 100%);
  }
  .portrait-area {
    position: absolute;
    right: 40px;
    top: 0;
    width: 300px;
    height: 320px;
    background: radial-gradient(ellipse at 50% 40%, #8a6a55 0%, #5b3f30 45%, rgba(199,176,159,0) 75%);
  }
  .front-brand {
    position: absolute;
    left: 34px;
    bottom: 70px;
    color: var(--card-white);
    font-size: 26px;
    font-weight: 500;
    letter-spacing: 0.5px;
  }
  /* Back face */
  .card-back {
    left: 610px;
    background: var(--card-white);
  }
  .back-brand {
    position: absolute;
    left: 110px;
    top: 62px;
    color: var(--gold);
    font-size: 32px;
    font-weight: 500;
    letter-spacing: 0.5px;
  }
  .qr-code {
    position: absolute;
    right: 26px;
    top: 26px;
    width: 86px;
    height: 86px;
    background: var(--qr-tint);
    border: 3px solid var(--gold);
    border-radius: 6px;
  }
  .identity {
    position: absolute;
    left: 28px;
    top: 168px;
    width: 210px;
    text-align: right;
  }
  .identity .name {
    color: var(--gold);
    font-size: 15px;
    font-weight: 700;
    text-transform: uppercase;
    letter-spacing: 0.3px;
  }
  .identity .role {
    color: var(--ink);
    font-size: 13px;
    margin-top: 4px;
  }
  .divider {
    position: absolute;
    left: 252px;
    top: 150px;
    width: 2px;
    height: 82px;
    background: var(--gold);
  }
  .contacts {
    position: absolute;
    left: 266px;
    top: 148px;
    list-style: none;
  }
  .contacts li {
    display: flex;
    align-items: center;
    gap: 8px;
    font-size: 12px;
    color: var(--ink);
    height: 28px;
  }
  .contacts svg { width: 14px; height: 14px; flex: none; }
  .appointment {
    position: absolute;
    left: 28px;
    right: 28px;
    top: 244px;
    display: flex;
    font-size: 12px;
    color: var(--ink);
    gap: 4px;
  }
  .appointment .fill {
    flex: 1;
    border-bottom: 2px dotted var(--ink);
    margin-bottom: 3px;
  }
  .address-band {
    position: absolute;
    left: 0;
    right: 0;
    bottom: 0;
    height: 46px;
    background: var(--band-brown);
    color: var(--card-white);
    font-size: 14px;
    font-weight: 500;
    display: flex;
    align-items: center;
    justify-content: center;
  }
</style>
</head>
<body>
  <section class="card card-front">
    <div class="portrait-area" role="img" aria-label="Portrait photograph of a woman with long curly hair"></div>
    <div class="front-brand">Verdant Medispa</div>
  </section>

  <section class="card card-back">
    <div class="back-brand">Verdant Medispa</div>
    <div class="qr-code" role="img" aria-label="QR code linking to the spa website"></div>

    <div class="identity">
      <div class="name">Sorina Belcourt, MD</div>
      <div class="role">Internal Medicine</div>
    </div>

    <div class="divider"></div>

    <ul class="contacts">
      <li>
        <svg viewBox="0 0 16 16"><path fill="var(--gold)" d="M3.5 1.5l2.5 0 1 3.5-1.8 1.2a8 8 0 0 0 4.6 4.6L11 9l3.5 1v2.5A2 2 0 0 1 12.5 14.5 11 11 0 0 1 1.5 3.5 2 2 0 0 1 3.5 1.5z"/></svg>
        555-204-7193
      </li>
      <li>
        <svg viewBox="0 0 16 16"><rect x="1" y="3.5" width="14" height="9" rx="1" fill="var(--gold)"/><path d="M1.5 4l6.5 5 6.5-5" stroke="#fff" stroke-width="1.2" fill="none"/></svg>
        Sorina@verdantmedispa-example.com
      </li>
      <li>
        <svg viewBox="0 0 16 16"><circle cx="8" cy="8" r="7" fill="var(--gold)"/><path d="M1 8h14M8 1c-3 3-3 11 0 14M8 1c3 3 3 11 0 14" stroke="#fff" stroke-width="0.9" fill="none"/></svg>
        Www.Verdantmedispa-example.com
      </li>
    </ul>

    <div class="appointment">
      <span>Date:</span><span class="fill"></span>
      <span>Time:</span><span class="fill"></span>
    </div>

    <div class="address-band">738 E Harlow Blvd N, Ste 512, Katy, TX 77981</div>
  </section>
</body>
</html>
```